Thornwick auto buffing and headlight restoration

I'm offering a service the will restore dull and discoloured headlights caused by sun damage. I also want to offer minor scratch repairs. $25 per headlight $10-$30 for scratches Mobile serviceI'd like to have an example of a dull and a new headlight. Clean colours eg. Blues,silver and whites.Very clean uncomplicated and professionals looking card. I'd like it to have a bold logo.

Target Market(s)

All car, truck and vehicle owners. Automotive industries.

Industry/Entity Type

Automotive

Contact Information for Business Card

(Front)
Headlight restoration and scratch Repair
Callum Thornwick
Mobile-0412 386 904
(Back)
Pricing
$25 per headlight
$10-$35 per scratch

Font styles to use
Sans Serif

Colors
85cae6
ffffff
0355a3
faa54b

Requirements
Must have
• Logo
• I would like my name to look confident. As if to say "I back myself"
• Bold easy to read text
• Clean lines
• Name -Callum Thornwick
• Phone- txt or call 0412386904
• Email- 47calt@mailverno.com
Nice to have
• I'm open to other color schemes
• 4 color scheme only
• Minimal orange
• Small amount of Silver if possible
• Bold outlined logo
Should not have
• Complex lines and logos

```html
<!DOCTYPE html>
<html lang="en">
<head>
<meta charset="utf-8">
<title>Thornwick Headlight Restoration – Business Card</title>
<link href="https://fonts.googleapis.com/css2?family=Advent+Pro:wght@300;400;500&family=Source+Sans+3:wght@600&display=swap" rel="stylesheet">
<style>
  :root {
    --page-bg: #ffffff;
    --label-blue: #1d4f9c;
    --headline-blue: #1f4fe6;
    --band-blue: rgba(108, 150, 240, 0.78);
    --text-white: #ffffff;
    --sky-deep: #4fa6d3;
    --sky-mid: #7cc6e6;
    --sky-light: #bfe8f5;
    --mist: #eef9fc;
  }
  * { margin: 0; padding: 0; box-sizing: border-box; }
  html, body {
    width: 800px;
    height: 1200px;
    overflow: hidden;
    background: var(--page-bg);
  }
  .sheet {
    position: relative;
    width: 800px;
    height: 1200px;
    font-family: "Advent Pro", "Arial Narrow", sans-serif;
  }
  .side-label {
    position: absolute;
    left: 30px;
    font-family: "Source Sans 3", Arial, sans-serif;
    font-weight: 600;
    font-size: 17px;
    color: var(--label-blue);
  }
  .side-label--front { top: 56px; }
  .side-label--back { top: 635px; }

  .card {
    position: absolute;
    left: 30px;
    width: 738px;
    height: 456px;
    overflow: hidden;
  }
  .card--front { top: 96px; }
  .card--back { top: 670px; }

  .card__photo {
    position: absolute;
    inset: 0;
  }
  .card--front .card__photo {
    background:
      radial-gradient(ellipse 40% 30% at 85% 20%, rgba(230, 248, 255, 0.55), transparent 70%),
      radial-gradient(ellipse 35% 25% at 15% 20%, rgba(210, 240, 252, 0.45), transparent 70%),
      radial-gradient(ellipse 60% 40% at 50% 95%, rgba(200, 240, 250, 0.6), transparent 70%),
      linear-gradient(180deg, var(--sky-deep) 0%, var(--sky-mid) 55%, var(--sky-light) 100%);
  }
  .card--back .card__photo {
    background:
      radial-gradient(ellipse 35% 30% at 45% 28%, rgba(240, 252, 255, 0.75), transparent 70%),
      radial-gradient(ellipse 55% 45% at 5% 95%, var(--mist), transparent 70%),
      radial-gradient(ellipse 40% 30% at 85% 15%, rgba(220, 245, 252, 0.5), transparent 70%),
      linear-gradient(180deg, var(--sky-deep) 0%, var(--sky-mid) 45%, var(--sky-light) 100%);
  }

  .text { position: absolute; line-height: 1; white-space: nowrap; }

  .headline {
    left: 149px;
    top: 191px;
    font-size: 57px;
    font-weight: 400;
    color: var(--headline-blue);
  }
  .subline {
    right: 153px;
    top: 252px;
    font-size: 33px;
    font-weight: 400;
    color: var(--headline-blue);
  }
  .contact-band {
    position: absolute;
    left: 0;
    top: 314px;
    width: 100%;
    height: 90px;
    background: var(--band-blue);
  }
  .contact__name {
    left: 152px;
    top: 335px;
    font-size: 26px;
    font-weight: 400;
    color: var(--text-white);
  }
  .contact__mobile {
    left: 152px;
    top: 368px;
    font-size: 18px;
    font-weight: 500;
    color: var(--text-white);
  }
  .contact__email {
    left: 349px;
    top: 348px;
    font-size: 21px;
    font-weight: 400;
    color: var(--text-white);
  }
  .divider {
    position: absolute;
    width: 0;
    border-left: 2px dotted var(--text-white);
  }
  .divider--contact { left: 328px; top: 322px; height: 66px; }
  .divider--pricing { left: 402px; top: 279px; height: 90px; }

  .pricing__label {
    left: 149px;
    top: 311px;
    font-size: 36px;
    font-weight: 400;
    color: var(--headline-blue);
  }
  .price {
    top: 287px;
    font-size: 53px;
    font-weight: 400;
    color: var(--headline-blue);
  }
  .price__unit {
    top: 346px;
    font-size: 23px;
    font-weight: 400;
    color: var(--text-white);
  }
  .price--headlight, .price__unit--headlight { left: 278px; }
  .price--scratch, .price__unit--scratch { left: 420px; }
</style>
</head>
<body>
<main class="sheet">
  <p class="side-label side-label--front">Front</p>
  <section class="card card--front">
    <div class="card__photo" role="img" aria-label="Photo of a car front with headlights on a blue textured background"></div>
    <h1 class="text headline">Headlight Restoration</h1>
    <p class="text subline">and Scratch Repair</p>
    <div class="contact-band"></div>
    <p class="text contact__name">Callum Thornwick</p>
    <p class="text contact__mobile">Mobile: 0412 386 904</p>
    <span class="divider divider--contact"></span>
    <p class="text contact__email">Email: 47calt@mailverno.com</p>
  </section>

  <p class="side-label side-label--back">Back</p>
  <section class="card card--back">
    <div class="card__photo" role="img" aria-label="Close-up photo of a car headlight on a blue textured background"></div>
    <p class="text pricing__label">Pricing:</p>
    <p class="text price price--headlight">$25</p>
    <p class="text price__unit price__unit--headlight">per headlight</p>
    <span class="divider divider--pricing"></span>
    <p class="text price price--scratch">$10 – $35</p>
    <p class="text price__unit price__unit--scratch">per scratch</p>
  </section>
</main>
</body>
</html>
```